verano living

I need a brochure that can help me sell memberships or enrollments into a delivery system for homes of natural products including flower arrangements and also hotel day passes . enclosed are the text and the current logo.

```html
<!DOCTYPE html>
<html lang="es">
<head>
<meta charset="utf-8">
<title>Verano Living – Membresía</title>
<link href="https://fonts.googleapis.com/css2?family=Roboto:wght@400;500;700&display=swap" rel="stylesheet">
<style>
  :root {
    --backdrop: #2a2a2a;
    --paper-light: #ffffff;
    --paper-shade: #e3e4e8;
    --olive-light: #a19b2f;
    --olive-mid: #87811d;
    --olive-dark: #6a6513;
    --ink: #4a4a4a;
    --heading: #555555;
    --rule: #6d6d6d;
    --brand-green: #4f8f2a;
  }
  * { box-sizing: border-box; margin: 0; padding: 0; }
  html, body { width: 1200px; height: 1200px; overflow: hidden; }
  body {
    background: var(--backdrop);
    font-family: "Roboto", Arial, sans-serif;
    position: relative;
  }
  .sheet {
    position: absolute;
    left: 159px; top: 30px;
    width: 988px; height: 1278px;
    transform: scale(0.892);
    transform-origin: top left;
    background: linear-gradient(160deg, var(--paper-light) 0%, #eef0f2 45%, var(--paper-shade) 100%);
    overflow: hidden;
    color: var(--ink);
  }
  .sheet-art { position: absolute; inset: 0; width: 988px; height: 1278px; }
  .brand-box {
    position: absolute; left: 732px; top: 48px; width: 256px; height: 83px;
    background: #fff;
    display: flex; align-items: center; justify-content: center; gap: 12px;
  }
  .brand-dot { width: 34px; height: 34px; border-radius: 50%; background: var(--brand-green); }
  .brand-name { font-size: 27px; font-weight: 500; color: var(--brand-green); letter-spacing: 0.5px; }
  .block { position: absolute; left: 50px; width: 888px; }
  .title { top: 180px; font-size: 29px; font-weight: 700; color: var(--heading); }
  .caps {
    font-size: 19.5px; line-height: 32px; text-transform: uppercase;
    text-align: justify; text-align-last: left;
  }
  .offer { top: 240px; }
  .saving { top: 385px; }
  .terms { font-size: 21px; line-height: 32.5px; text-align: justify; text-align-last: left; }
  .accept { top: 494px; }
  .recurring { top: 623px; }
  .delivery { top: 924px; }
  .complaint { top: 1021px; width: 920px; }
  .blank { display: inline-block; border-bottom: 1px solid var(--rule); height: 1em; vertical-align: baseline; }
  .card-table {
    position: absolute; left: 198px; top: 720px; width: 592px;
    border-collapse: collapse; font-size: 21px; color: var(--ink);
  }
  .card-table td { border: 1px solid var(--rule); height: 60px; padding: 0 19px; }
  .card-table td:first-child { width: 192px; }
  .signature { position: absolute; left: 77px; top: 1187px; width: 280px; border-top: 1px solid var(--rule); text-align: center; font-size: 27px; padding-top: 0; line-height: 30px; }
</style>
</head>
<body>
  <div class="sheet">
    <svg class="sheet-art" viewBox="0 0 988 1278" aria-hidden="true">
      <path d="M300 0 C 120 500, 80 900, 0 1278 L 90 1278 C 170 900, 230 450, 420 0 Z" fill="#ffffff" opacity="0.45"/>
      <path d="M988 420 C 700 700, 300 900, 0 1100 L 0 1150 C 350 950, 750 760, 988 520 Z" fill="#ffffff" opacity="0.5"/>
      <path d="M0 1100 C 300 1030, 650 1050, 988 1060 L 988 1278 L 0 1278 Z" fill="#ffffff" opacity="0.8"/>
      <path d="M0 0 H 665 C 520 70, 420 150, 260 147 C 150 145, 60 110, 0 98 Z" fill="var(--olive-dark)"/>
      <path d="M0 0 H 600 C 470 60, 380 120, 250 118 C 150 116, 60 80, 0 68 Z" fill="var(--olive-mid)"/>
      <path d="M0 0 H 520 C 420 45, 340 85, 230 82 C 140 80, 60 45, 0 32 Z" fill="var(--olive-light)"/>
      <path d="M240 1278 C 480 1180, 760 1085, 988 1075 V 1278 Z" fill="var(--olive-dark)"/>
      <path d="M330 1278 C 540 1200, 780 1120, 988 1112 V 1278 Z" fill="var(--olive-mid)"/>
      <path d="M470 1278 C 640 1215, 820 1165, 988 1160 V 1278 Z" fill="var(--olive-light)"/>
    </svg>

    <div class="brand-box">
      <span class="brand-dot"></span>
      <span class="brand-name">verano living</span>
    </div>

    <h1 class="block title">Y COMO REGALO DE FIDELIDAD</h1>

    <p class="block caps offer">Como regalo de aniversario al completar 24 meses ininterrumpidos de servicios, se le otorgara un certificado para que pueda estar hospedado por un periodo de 3 dias y 2 noches en plan todo incluido, para dos adultos en los hoteles del Grupo Marea Alta.</p>

    <p class="block caps saving">Por todo esto, con los ahorros que obtendras con nuestros productos y servicios, la inversion se convertira en un ahorro.</p>

    <p class="block terms accept">Yo <span class="blank" style="width:424px"></span>, acepto pertenecer al Club Verano Living, por lo cual autorizo un cargo mensual a mi TC por un importe de $ <span class="blank" style="width:70px"></span>.00 que será cargado el dia <span style="display:inline-block;width:96px"></span>.</p>

    <p class="block terms recurring">Estoy de acuerdo que el cargo será recurrente hasta que cancele mi suscripción, dando aviso al correo <span class="blank" style="width:424px"></span> , con 30 días de anticipación.</p>

    <table class="card-table">
      <tr><td>TARJETA</td><td></td></tr>
      <tr><td>VENCIMIENTO</td><td></td></tr>
      <tr><td>CODIGO</td><td></td></tr>
    </table>

    <p class="block terms delivery">Así mismo, estoy de acuerdo que los días de entrega serán los días <span class="blank" style="width:70px"></span> , del mes en curso a mi domicilio en <span class="blank" style="width:424px"></span><span style="display:inline-block;width:236px"></span>.</p>

    <p class="block terms complaint">Cualquier queja del servicio producto o la entrega será dirigido a <span class="blank" style="width:234px"></span> <span style="display:inline-block;width:8px"></span>.</p>

    <div class="signature">Firma</div>
  </div>
</body>
</html>
```